Rug Cleaning Web Design Project

We need a web design for our cleaning company. We currently have a web page but are not happy with its design. We currently offer fine rug cleaning,upholstery cleaning, and residential and commercial carpet cleanning. We also offer water damage restoration. For our rug cleaning services we offer : Enzyme treatments for pet contamination and odor removal, application of stain protection that is designed for the fine textiles used in rug construction, application of treatments designed to prevent moth damage and pads designed to be used under rugs.Our current web site is harborfreshcare.example. We are intrested in a design with similar information to the web page of Velmora Rug Cleaners INC. We would like to use the colors that are present in our logo that will be uploaded with this description. We would also like this new page to be linked to our other address loomrinsepro.example. We would like the deign to be visually attractive but not "too busy".
Updates

Please include pictures of rugs, or people washing rugs if possible. We do not offer maid type cleaning services. We would not be interested in designs including pictures depicting that type service. Thanks for your hard work on this project.

Dana Whitlow

Industry/Entity Type

Residential

Requirements
Must have
• This page must be viewable on smart phones and tablets.

```html
<!DOCTYPE html>
<html lang="en">
<head>
<meta charset="utf-8">
<meta name="viewport" content="width=device-width, initial-scale=1">
<title>LoomRinse Pro – Fine Rug Cleaning</title>
<link rel="stylesheet" href="https://fonts.googleapis.com/css2?family=Open+Sans:wght@400;600;700&family=Roboto+Condensed:wght@400;700&display=swap">
<style>
:root{
  --blue:#1b6fc1;
  --blue-dark:#0d4f97;
  --blue-deep:#0a3f7c;
  --orange:#f7a600;
  --orange-light:#ffd200;
  --gold:#f2c230;
  --page:#ececec;
  --panel:#ffffff;
  --ink:#1d1d1d;
  --muted:#5a5a5a;
  --brown:#7a3510;
  --green:#7fe07c;
  --heading-blue:#1a6dbd;
}
*{box-sizing:border-box;margin:0;padding:0}
html,body{width:1200px;height:1093px;overflow:hidden}
body{position:relative;background:var(--page);font-family:"Open Sans",Arial,sans-serif;color:var(--ink)}
.abs{position:absolute}

/* header */
.header{left:0;top:0;width:1200px;height:106px;background:#f7f7f7}
.brand{left:35px;top:14px;display:flex;align-items:center;gap:14px}
.brand-mark{width:58px;height:58px;border-radius:50%;background:var(--blue)}
.brand-name{font-weight:700;font-size:40px;color:#222;letter-spacing:-1px;line-height:1}
.brand-sub{font-size:12px;letter-spacing:4px;color:#555;margin-top:2px}
.award{left:408px;top:0;width:290px;height:100px}
.award-badge{position:absolute;left:0;top:10px;width:44px;height:44px;border-radius:50%;background:var(--gold)}
.award-title{position:absolute;left:54px;top:10px;font-family:"Roboto Condensed",sans-serif;font-size:30px;line-height:36px;color:#333;white-space:nowrap}
.award-sub{position:absolute;left:60px;top:50px;font-weight:600;font-size:19px;line-height:26px;color:#2a2a2a;white-space:nowrap}
.email{right:38px;top:12px;font-size:16px;color:#111}
.callbox{left:692px;top:46px;width:508px;height:60px}
.call-text{position:absolute;left:40px;top:10px;font-family:"Roboto Condensed",sans-serif;font-size:35px;color:var(--green);white-space:nowrap}

/* nav */
.nav{left:0;top:106px;width:1200px;height:65px;background:var(--blue);display:flex;padding-left:35px}
.nav a{display:block;height:65px;line-height:65px;padding:0 25px;font-family:"Roboto Condensed",sans-serif;font-size:19px;color:#fff;text-decoration:none;border-right:1px solid #2c7ed0}
.nav a.active{background:linear-gradient(#ffc21a,#f39a00);color:#222;padding:0 20px}

/* slider */
.slider{left:23px;top:181px;width:1154px;height:434px;background:var(--blue)}
.slider-inner{position:absolute;left:12px;top:12px;width:1130px;height:410px;background:#e6e6e6}
.slider-photo{position:absolute;left:0;top:0;width:763px;height:410px;background:linear-gradient(135deg,#d9cdb8 0%,#a47b56 45%,#6a3a2a 75%,#3a3236 100%)}
.slider-copy{position:absolute;left:786px;top:14px;width:318px;text-align:center}
.slider-copy h1{font-weight:400;font-size:37px;line-height:42px;color:var(--brown)}
.slider-copy p{margin-top:10px;font-size:16px;line-height:32px;color:#666}
.read-more{position:absolute;right:40px;top:282px;font-size:15px;font-weight:600;color:#333}
.dots{position:absolute;left:877px;top:384px;display:flex;gap:6px}
.dots span{width:15px;height:15px;background:var(--blue);border:1px solid #fff}
.dots span.on{background:var(--orange)}

/* band */
.band-line{left:0;top:632px;width:1200px;height:1px;background:#d0d0d0}
.card{top:648px;height:290px;background:var(--panel);box-shadow:0 1px 3px rgba(0,0,0,.2)}
.welcome{left:35px;width:371px;padding:14px 16px}
.welcome h2{text-align:center;font-weight:400;font-size:25px;color:var(--heading-blue);margin-bottom:10px}
.welcome p{font-size:13.5px;line-height:21px;color:#555}
.card-head{height:43px;line-height:43px;text-align:center;font-size:25px}
.services{left:416px;width:370px}
.services .card-head{background:linear-gradient(#2a82d4,#155fae);color:#fff}
.tiles{display:grid;grid-template-columns:173px 173px;gap:6px 11px;padding:6px 6px 0 6px}
.tile{position:relative;height:113px;color:#fff;text-align:center}
.tile svg{position:absolute;left:68px;top:28px}
.tile span{position:absolute;left:0;right:0;bottom:6px;font-size:16.5px}
.t1{background:linear-gradient(#4a2c22,#2b1e1c)}
.t2{background:linear-gradient(#3a3a3a,#1c1c1c)}
.t3{background:linear-gradient(#5a4a3a,#2e2a27)}
.t4{background:linear-gradient(#8a7a66,#4a3e34)}
.why{left:796px;width:372px}
.why .card-head{background:linear-gradient(var(--orange-light),var(--orange));color:#1a1a1a}
.why ul{list-style:none;padding:12px 0 0 22px}
.why li{font-size:14px;line-height:25.5px;color:#555;display:flex;align-items:center;gap:9px;white-space:nowrap}

/* footer */
.footer{left:0;top:967px;width:929px;height:63px;background:var(--blue);text-align:center;color:#fff;font-size:13px;padding-top:10px;padding-left:120px}
.footer nav{margin-bottom:6px}
.footer a{color:#fff;text-decoration:none}
.foot-brand{left:692px;top:1030px;width:237px;height:63px}
.foot-brand-text{position:absolute;left:42px;top:16px;display:flex;align-items:center;gap:8px;font-weight:700;font-size:20px;color:#fff;white-space:nowrap}
.foot-brand-text i{width:22px;height:22px;border-radius:50%;background:#3a8be0;display:block}
.map{left:929px;top:967px;width:248px;height:126px;background:linear-gradient(135deg,#9aa6a6,#7d8f98);color:#fff;text-align:center}
.map svg{position:absolute;left:104px;top:44px}
.map-name{position:absolute;left:0;right:0;top:84px;font-size:12.5px;white-space:nowrap}
.map-addr{position:absolute;left:0;right:0;top:104px;font-size:12.5px;white-space:nowrap}
</style>
</head>
<body>

<header class="abs header">
  <div class="abs brand">
    <div class="brand-mark"></div>
    <div>
      <div class="brand-name">LoomRinse Pro</div>
      <div class="brand-sub">HARBOR FRESH CARE, LLC</div>
    </div>
  </div>
  <div class="abs award">
    <div class="award-badge"></div>
    <div class="award-title">1st best in business award</div>
    <div class="award-sub">Consumers first choice</div>
  </div>
  <div class="abs email">Email Us: hello@harborfreshcare.example</div>
  <div class="abs callbox">
    <svg width="508" height="60" viewBox="0 0 508 60" style="position:absolute;left:0;top:0">
      <polygon points="24,0 508,0 508,60 0,60" fill="var(--blue-dark)"/>
      <polygon points="24,0 508,0 508,4 21,4" fill="#0a3566"/>
    </svg>
    <div class="call-text">Give Us a Call : (555)-014-2290</div>
  </div>
</header>

<nav class="abs nav">
  <a class="active" href="#">Home</a>
  <a href="#">About Us</a>
  <a href="#">Rug Washing</a>
  <a href="#">Water Damage</a>
  <a href="#">Carpet Cleaning</a>
  <a href="#">Our Location</a>
  <a href="#">Contact Us</a>
</nav>

<section class="abs slider">
  <div class="slider-inner">
    <div class="slider-photo" role="img" aria-label="Worker squeegeeing an oriental rug on the washing floor of a rug cleaning plant, rugs hanging to dry behind"></div>
    <div class="slider-copy">
      <h1>We specialize in Fine Rug Cleaning</h1>
      <p>Oriental and Speciality Rugs differ greatly in their construction, dyeing methods and fiber content...and we understand these differences, assuring a safe and thorough in-plant cleaning of your speciality rugs.</p>
    </div>
    <div class="read-more">Read more</div>
    <div class="dots"><span class="on"></span><span></span><span></span><span></span><span></span></div>
  </div>
</section>

<div class="abs band-line"></div>

<section class="abs card welcome">
  <h2>Welcome to LoomRinse Pro</h2>
  <p>When it comes to cleaning carpet, oriental rugs, area rugs or furniture ~ any fabric from antique silk brocades to contemporary carpet fibers ~ our service is unparalled.<br>
  Harbor Fresh Care &amp; Restoration is the recipient of the 2010 &amp; 2011<br>
  "Best in Business Award" in Marlow Falls, Westland for Water Damage Restoration and Carpet and Rug Cleaning.<br>
  &nbsp;Please contact us for an extensive list of references.</p>
</section>

<section class="abs card services">
  <div class="card-head">Our Services</div>
  <div class="tiles">
    <div class="tile t1" role="img" aria-label="Stack of patterned rugs">
      <svg width="38" height="38" viewBox="0 0 38 38"><circle cx="19" cy="19" r="17" fill="none" stroke="#fff" stroke-width="2.5"/><path d="M19 10v18M10 19h18" stroke="#fff" stroke-width="3.5"/></svg>
      <span>Rug Cleaning</span>
    </div>
    <div class="tile t2" role="img" aria-label="Water leaking from a pipe">
      <svg width="38" height="38" viewBox="0 0 38 38"><circle cx="19" cy="19" r="17" fill="none" stroke="#fff" stroke-width="2.5"/><path d="M19 10v18M10 19h18" stroke="#fff" stroke-width="3.5"/></svg>
      <span>Water damage</span>
    </div>
    <div class="tile t3" role="img" aria-label="Technician cleaning a carpet">
      <svg width="38" height="38" viewBox="0 0 38 38"><circle cx="19" cy="19" r="17" fill="none" stroke="#fff" stroke-width="2.5"/><path d="M19 10v18M10 19h18" stroke="#fff" stroke-width="3.5"/></svg>
      <span>Carpet Cleaning</span>
    </div>
    <div class="tile t4" role="img" aria-label="Upholstered armchairs in a living room">
      <svg width="38" height="38" viewBox="0 0 38 38"><circle cx="19" cy="19" r="17" fill="none" stroke="#fff" stroke-width="2.5"/><path d="M19 10v18M10 19h18" stroke="#fff" stroke-width="3.5"/></svg>
      <span>Upholstery Cleaning</span>
    </div>
  </div>
</section>

<section class="abs card why">
  <div class="card-head">Why Choose Us?</div>
  <ul>
    <li><svg width="10" height="8" viewBox="0 0 10 8"><path d="M0 4h8M5 1l3 3-3 3" fill="none" stroke="#777" stroke-width="1.2" stroke-dasharray="2 1"/></svg>Maecenas laoreet mauris eu risus Elementum</li>
    <li><svg width="10" height="8" viewBox="0 0 10 8"><path d="M0 4h8M5 1l3 3-3 3" fill="none" stroke="#777" stroke-width="1.2" stroke-dasharray="2 1"/></svg>Nulla facilisi. Vestibulum quis est dapibus mauris</li>
    <li><svg width="10" height="8" viewBox="0 0 10 8"><path d="M0 4h8M5 1l3 3-3 3" fill="none" stroke="#777" stroke-width="1.2" stroke-dasharray="2 1"/></svg>Vestibulum pellentesque vitae quis Nulla</li>
    <li><svg width="10" height="8" viewBox="0 0 10 8"><path d="M0 4h8M5 1l3 3-3 3" fill="none" stroke="#777" stroke-width="1.2" stroke-dasharray="2 1"/></svg>Maecenas lorem nisl, maleSuada eu porta a,</li>
    <li><svg width="10" height="8" viewBox="0 0 10 8"><path d="M0 4h8M5 1l3 3-3 3" fill="none" stroke="#777" stroke-width="1.2" stroke-dasharray="2 1"/></svg>Volutpat nec orci. Vivamus feugiat sollicitudin</li>
    <li><svg width="10" height="8" viewBox="0 0 10 8"><path d="M0 4h8M5 1l3 3-3 3" fill="none" stroke="#777" stroke-width="1.2" stroke-dasharray="2 1"/></svg>Ultrices. Proin vitae nibh a lectus porttitor</li>
    <li><svg width="10" height="8" viewBox="0 0 10 8"><path d="M0 4h8M5 1l3 3-3 3" fill="none" stroke="#777" stroke-width="1.2" stroke-dasharray="2 1"/></svg>Placerat et in elit. Nullam accumsan, lorem ut</li>
    <li><svg width="10" height="8" viewBox="0 0 10 8"><path d="M0 4h8M5 1l3 3-3 3" fill="none" stroke="#777" stroke-width="1.2" stroke-dasharray="2 1"/></svg>Sagittis commodo, ante magna tempor massa, in</li>
  </ul>
</section>

<footer class="abs footer">
  <nav><a href="#">Home</a> &nbsp;/&nbsp; <a href="#">About Us</a> &nbsp;/&nbsp; <a href="#">Rug Washing</a> &nbsp;/&nbsp; <a href="#">Water Damage</a> &nbsp;/&nbsp; <a href="#">Carpet Cleaning</a> &nbsp;/&nbsp; <a href="#">Our Location</a> &nbsp;/&nbsp; <a href="#">Contact Us</a></nav>
  <div>Copyrights &nbsp;2012-2013 LoomRinse Pro. All Rights Reserved</div>
</footer>

<div class="abs foot-brand">
  <svg width="237" height="63" viewBox="0 0 237 63" style="position:absolute;left:0;top:0">
    <polygon points="0,0 237,0 237,63 28,63" fill="var(--blue-deep)"/>
  </svg>
  <div class="foot-brand-text"><i></i>LoomRinse Pro</div>
</div>

<div class="abs map" role="img" aria-label="Street map showing the shop location">
  <svg width="40" height="40" viewBox="0 0 40 40"><circle cx="20" cy="20" r="18" fill="none" stroke="#fff" stroke-width="2.5"/><path d="M20 10v20M10 20h20" stroke="#fff" stroke-width="3.5"/></svg>
  <div class="map-name">Harbor Fresh Care &amp; Restoration</div>
  <div class="map-addr">48 Quarry Lane,Elmsford, WL 00000</div>
</div>

</body>
</html>
```